Brochure

I have a current booklet for Cedar Peak Labs, I need to incorporate additional information and testing into it. attached are the current inside pages and the additional items that need to be added.

Requirements
Must have
• matching the background, colors, and format of the original inside booklet pages.

```html
<!DOCTYPE html>
<html lang="en">
<head>
<meta charset="utf-8">
<title>Cedar Peak Labs – Test Panel Booklet Pages</title>
<link href="https://fonts.googleapis.com/css2?family=Poppins:wght@400;500;600;700;800&display=swap" rel="stylesheet">
<style>
:root{
  --stage:#b2b2b2;
  --paper:#ffffff;
  --brand-blue:#1f78cc;
  --title-blue:#2479cf;
  --sky:#5fc3f0;
  --tab-gray:#50545a;
  --cell-gray:#e9e9ea;
  --ink:#2f3236;
  --photo-a:#c9d8e6;
  --photo-b:#8aa6c0;
}
*{margin:0;padding:0;box-sizing:border-box}
html,body{width:957px;height:1200px;overflow:hidden}
body{background:var(--stage);font-family:'Poppins',sans-serif;color:var(--ink);position:relative}
.page{position:absolute;width:612px;height:792px;background:var(--paper);transform:scale(.638);transform-origin:0 0;overflow:hidden}
.page--abr{left:78.5px;top:44.7px}
.page--nail{left:497px;top:44.7px}
.page--uti{left:83px;top:594.6px}
.page--wound{left:495px;top:594.6px}
.abs{position:absolute}
.shapes{position:absolute;left:0;top:0;width:612px;height:792px}
.brand{position:absolute;display:flex;flex-direction:column;align-items:center;width:110px}
.brand__mark{width:26px;height:26px;border:2px solid var(--brand-blue);border-radius:50%}
.brand__name{margin-top:3px;font-weight:600;font-size:14px;color:var(--brand-blue);letter-spacing:.2px;white-space:nowrap;text-align:center;line-height:1.05}
.page-title{position:absolute;font-weight:700;font-size:24px;color:var(--title-blue);line-height:1.2;text-transform:uppercase}
.targets{position:absolute;font-weight:700;font-size:18px}
.lede{position:absolute;font-size:9.5px;line-height:1.25;font-weight:500}
.on-blue{color:#fff}
.section{position:absolute;font-weight:600;font-size:14px;color:var(--title-blue);text-transform:uppercase}
.list{position:absolute;list-style:none;font-size:9.6px;font-weight:500}
.list li{position:relative;padding-left:11px;min-height:19px;line-height:1.2}
.list li::before{content:"";position:absolute;left:0;top:4px;width:5px;height:5px;border-radius:50%;background:var(--brand-blue)}
.tab{position:absolute;writing-mode:vertical-rl;color:#fff;font-weight:700;font-size:14.5px;white-space:nowrap}
.photo{position:absolute;background:linear-gradient(135deg,var(--photo-a),var(--photo-b))}
.gene-table{position:absolute;left:52px;top:252px;border-collapse:separate;border-spacing:0 3.6px;font-size:9.6px}
.gene-table td{height:20px;padding:0 8px}
.gene-table .code{width:86px;background:var(--brand-blue);color:#fff;font-weight:500}
.gene-table .effect{width:160px;background:var(--cell-gray);border-left:4px solid #fff}
.features{position:absolute;list-style:none}
.feature{display:flex;align-items:center;gap:10px;font-size:9.6px;line-height:1.25;margin-bottom:14px}
.feature svg{flex:0 0 30px;width:30px;height:30px}
.feature b{font-weight:700}
.pg-num{position:absolute;font-size:9.5px;font-weight:500}
</style>
</head>
<body>

<!-- Page 01: Antibiotic resistance gene -->
<section class="page page--abr">
  <svg class="shapes" viewBox="0 0 612 792">
    <defs>
      <linearGradient id="sea1" x1="0" x2="1"><stop offset="0" stop-color="#1f78cc"/><stop offset=".6" stop-color="#3ea5e6"/><stop offset="1" stop-color="#8ad8f6"/></linearGradient>
    </defs>
    <polygon points="0,730 612,700 612,792 0,792" fill="url(#sea1)"/>
    <polygon points="0,760 612,735 612,792 0,792" fill="#1766b5" opacity=".35"/>
    <rect x="558" y="0" width="54" height="592" fill="var(--tab-gray)"/>
    <polygon points="612,560 612,762 285,762" fill="var(--tab-gray)"/>
  </svg>
  <div class="brand" style="left:50px;top:36px"><span class="brand__mark"></span><span class="brand__name">CEDAR PEAK LABS</span></div>
  <h1 class="page-title" style="left:53px;top:106px">Antibiotic Resistance Gene</h1>
  <div class="targets" style="left:53px;top:152px;color:var(--title-blue);font-size:14px">12 TARGETS</div>
  <p class="lede" style="left:53px;top:176px;width:240px">A provider's #1 priority is their patients. When you bring them more targets, you are providing them better tools for treatment</p>
  <div class="section" style="left:53px;top:228px">ABR</div>
  <table class="gene-table">
    <tr><td class="code">KPC</td><td class="effect">Carbapenem resistance</td></tr>
    <tr><td class="code">NDM</td><td class="effect">Carbapenem resistance</td></tr>
    <tr><td class="code">VIM</td><td class="effect">Carbapenem resistance</td></tr>
    <tr><td class="code">IMP</td><td class="effect">Carbapenem resistance</td></tr>
    <tr><td class="code">qnr</td><td class="effect">Quinolone resistance</td></tr>
    <tr><td class="code">vanB</td><td class="effect">Vancomycin resistance</td></tr>
    <tr><td class="code">OXA</td><td class="effect">48 - Carbapenem resistance</td></tr>
    <tr><td class="code">mecA/mecC</td><td class="effect">Methicillin resistance</td></tr>
    <tr><td class="code">CTX</td><td class="effect">M ESBL</td></tr>
    <tr><td class="code">sul</td><td class="effect">Sulfonamide resistance</td></tr>
    <tr><td class="code">vanA</td><td class="effect">Vancomycin resistance</td></tr>
    <tr><td class="code">dfrA</td><td class="effect">Trimethoprim resistance</td></tr>
  </table>
  <div class="photo" role="img" aria-label="Smiling physician in a white coat holding a clipboard" style="left:329px;top:158px;width:204px;height:219px;border:1px solid #999"></div>
  <div class="photo" role="img" aria-label="Gloved hand loading sample tubes into an automated PCR instrument" style="left:329px;top:387px;width:204px;height:335px;background:linear-gradient(160deg,#3f6fb5,#9cc0e6 55%,#eef2f5)"></div>
  <ul class="features" style="left:52px;top:562px">
    <li class="feature"><svg viewBox="0 0 30 30"><circle cx="15" cy="15" r="13" fill="none" stroke="#1f78cc" stroke-width="1.6"/><path d="M10 20v-5M14 20v-8M18 20v-6" stroke="#1f78cc" stroke-width="2"/></svg><p><b>Cost effective</b> to help maximize your<br>lab's <b>profits</b></p></li>
    <li class="feature"><svg viewBox="0 0 30 30"><circle cx="15" cy="15" r="13" fill="none" stroke="#1f78cc" stroke-width="1.6"/><path d="M10 20v-4M14 20v-7M18 20v-10" stroke="#1f78cc" stroke-width="2"/></svg><p><b>‹45 minute</b> run time ensures <b>faster</b><br>turnaround times</p></li>
    <li class="feature"><svg viewBox="0 0 30 30"><circle cx="15" cy="15" r="13" fill="none" stroke="#1f78cc" stroke-width="1.6"/><circle cx="15" cy="15" r="6" fill="none" stroke="#1f78cc" stroke-width="1.6"/><path d="M15 9v12M9 15h12" stroke="#1f78cc" stroke-width="1.2"/></svg><p>Compatible with ALL PCR <b>MACHINES</b></p></li>
    <li class="feature"><svg viewBox="0 0 30 30"><circle cx="15" cy="15" r="13" fill="none" stroke="#1f78cc" stroke-width="1.6"/><path d="M10 20l5-9 5 9z" fill="none" stroke="#1f78cc" stroke-width="1.6"/></svg><p><b>Highly demanded</b> targets to make<br>your lab <b>more appealing to providers</b></p></li>
  </ul>
  <div class="pg-num" style="left:548px;top:728px;color:#fff">01</div>
  <div class="tab" style="left:575px;top:228px">Tabs Here - This portion will be trimmed off</div>
</section>

<!-- Page 02: Nail / fungal -->
<section class="page page--nail">
  <svg class="shapes" viewBox="0 0 612 792">
    <defs>
      <linearGradient id="sea2" x1="0" x2="1"><stop offset="0" stop-color="#1f78cc"/><stop offset="1" stop-color="#3fa0e4"/></linearGradient>
      <linearGradient id="ph2" x1="0" x2="1" y1="0" y2="1"><stop offset="0" stop-color="#5b8fcf"/><stop offset=".5" stop-color="#e3c9b5"/><stop offset="1" stop-color="#a9b6c2"/></linearGradient>
    </defs>
    <polygon points="130,0 612,0 612,340" fill="url(#ph2)" role="img" aria-label="Podiatrist using a rotary file on a patient's toenail"/>
    <line x1="130" y1="0" x2="612" y2="345" stroke="#1f78cc" stroke-width="6"/>
    <polygon points="44,164 350,164 505,280 44,280" fill="var(--brand-blue)"/>
    <polygon points="44,690 612,775 612,792 44,792" fill="url(#sea2)"/>
    <rect x="0" y="0" width="44" height="792" fill="var(--tab-gray)"/>
  </svg>
  <div class="tab" style="left:15px;top:134px">Tabs Here - This portion will be trimmed off</div>
  <div class="brand" style="left:64px;top:36px"><span class="brand__mark"></span><span class="brand__name">CEDAR PEAK LABS</span></div>
  <h1 class="page-title" style="left:66px;top:110px">Nail/Fungal</h1>
  <div class="targets on-blue" style="left:66px;top:180px">12 TARGETS</div>
  <p class="lede on-blue" style="left:66px;top:216px;width:260px">A provider's #1 priority is their patients. When you bring them more targets, you are providing them better tools for treatment</p>
  <div class="section" style="left:63px;top:301px">Fungi</div>
  <ul class="list" style="left:64px;top:325px">
    <li>Microsporum gypseum</li><li>Microsporum canis/ audouinii</li><li>Trichophyton spp</li><li>Malassezia furfur</li><li>Malassezia sympodialis</li><li>Candida krusei</li><li>Candida albicans</li><li>Candida glabrata</li><li>Candida parapsilosis</li>
  </ul>
  <ul class="list" style="left:242px;top:325px">
    <li>Candida auris</li><li>Aspergillus niger</li><li>Aspergillus flavus</li><li>Aspergillus fumigatus</li><li>Aspergillus terreus</li><li>Epidermophyton floccosum</li><li>Fusarium oxysporum</li><li>Trichosporon asahii</li><li>Trichosporon mucoides</li>
  </ul>
  <ul class="features" style="left:410px;top:320px">
    <li class="feature"><svg viewBox="0 0 30 30"><circle cx="15" cy="15" r="13" fill="none" stroke="#1f78cc" stroke-width="1.6"/><path d="M10 20v-5M14 20v-8M18 20v-6" stroke="#1f78cc" stroke-width="2"/></svg><p><b>Cost effective</b><br>to help maximize<br>your lab's <b>profits</b></p></li>
    <li class="feature"><svg viewBox="0 0 30 30"><circle cx="15" cy="15" r="13" fill="none" stroke="#1f78cc" stroke-width="1.6"/><path d="M10 20v-4M14 20v-7M18 20v-10" stroke="#1f78cc" stroke-width="2"/></svg><p><b>‹45 minute</b> run time<br>ensures <b>faster</b><br>turnaround times</p></li>
    <li class="feature"><svg viewBox="0 0 30 30"><circle cx="15" cy="15" r="13" fill="none" stroke="#1f78cc" stroke-width="1.6"/><circle cx="15" cy="15" r="6" fill="none" stroke="#1f78cc" stroke-width="1.6"/><path d="M15 9v12M9 15h12" stroke="#1f78cc" stroke-width="1.2"/></svg><p>Compatible with<br>ALL PCR <b>MACHINES</b></p></li>
    <li class="feature"><svg viewBox="0 0 30 30"><circle cx="15" cy="15" r="13" fill="none" stroke="#1f78cc" stroke-width="1.6"/><path d="M10 20l5-9 5 9z" fill="none" stroke="#1f78cc" stroke-width="1.6"/></svg><p><b>Highly demanded</b><br>targets to make<br>your lab <b>more</b><br><b>appealing to providers</b></p></li>
  </ul>
  <div class="photo" role="img" aria-label="Gloved hands trimming a fungal toenail with nippers" style="left:77px;top:523px;width:235px;height:182px;background:linear-gradient(135deg,#6d8fd6,#e6cbb6 55%,#c9a98f)"></div>
  <div class="photo" role="img" aria-label="Close-up of nippers cutting a toenail" style="left:323px;top:523px;width:235px;height:182px;background:linear-gradient(135deg,#e9d6c7,#d8b49c 60%,#f1e6dc)"></div>
  <div class="pg-num" style="left:62px;top:752px;color:#fff">02</div>
</section>

<!-- Page 03: Urinary tract infection -->
<section class="page page--uti">
  <svg class="shapes" viewBox="0 0 612 792">
    <defs>
      <linearGradient id="sea3" x1="0" x2="1"><stop offset="0" stop-color="#bfe6f7"/><stop offset=".5" stop-color="#4fb4ea"/><stop offset="1" stop-color="#1f78cc"/></linearGradient>
    </defs>
    <rect x="0" y="181" width="558" height="114" fill="var(--brand-blue)"/>
    <polygon points="40,792 558,700 558,792" fill="url(#sea3)"/>
    <rect x="558" y="0" width="54" height="792" fill="var(--tab-gray)"/>
  </svg>
  <div class="brand" style="left:50px;top:36px"><span class="brand__mark"></span><span class="brand__name">CEDAR PEAK LABS</span></div>
  <h1 class="page-title" style="left:53px;top:108px">Urinary Tract<br>Infection</h1>
  <div class="photo" role="img" aria-label="Illustration of kidneys and bladder with a stethoscope" style="left:302px;top:50px;width:228px;height:213px;border:2px solid #fff;background:linear-gradient(135deg,#e7eef6,#c7d6e8 50%,#e6b7b7)"></div>
  <div class="targets on-blue" style="left:53px;top:200px">28 TARGETS</div>
  <p class="lede on-blue" style="left:53px;top:228px;width:235px">A provider's #1 priority is their patients. When you bring them more targets, you are providing them better tools for treatment</p>
  <div class="section" style="left:51px;top:330px">Bacteria</div>
  <ul class="list" style="left:51px;top:356px">
    <li>Escherichia coli</li><li>Streptococcus agalactiae</li><li>Klebsiella oxytoca</li><li style="min-height:31px">Staphylococcus<br>saprophyticus</li><li>Serratia marcescens</li><li>Proteus mirabilis</li><li>Aerococcus urinae</li><li>Treponema pallidum</li>
  </ul>
  <ul class="list" style="left:217px;top:356px">
    <li>Enterobacter cloacae</li><li>Pseudomonas aeruginosa</li><li>Citrobacter freundii</li><li>Klebsiella aerogenes</li><li>Klebsiella pneumoniae</li><li>Morganella morganii</li><li>Corynebacterium<br>urealyticum</li>
  </ul>
  <ul class="list" style="left:393px;top:356px">
    <li>Enterococcus faecium</li><li>Enterococcus faecalis</li><li>Acinetobacter baumannii</li><li>Proteus vulgaris</li><li>Staphylococcus aureus</li><li>Ureplasma</li><li>Providencia stuartii</li>
  </ul>
  <ul class="features" style="left:50px;top:536px">
    <li class="feature"><svg viewBox="0 0 30 30"><circle cx="15" cy="15" r="13" fill="none" stroke="#1f78cc" stroke-width="1.6"/><path d="M10 20v-5M14 20v-8M18 20v-6" stroke="#1f78cc" stroke-width="2"/></svg><p><b>Cost effective</b><br>to help maximize<br>your lab's <b>profits</b></p></li>
    <li class="feature"><svg viewBox="0 0 30 30"><circle cx="15" cy="15" r="13" fill="none" stroke="#1f78cc" stroke-width="1.6"/><path d="M10 20v-4M14 20v-7M18 20v-10" stroke="#1f78cc" stroke-width="2"/></svg><p><b>‹45 minute</b> run time<br>ensures <b>faster</b><br>turnaround times</p></li>
    <li class="feature"><svg viewBox="0 0 30 30"><circle cx="15" cy="15" r="13" fill="none" stroke="#1f78cc" stroke-width="1.6"/><circle cx="15" cy="15" r="6" fill="none" stroke="#1f78cc" stroke-width="1.6"/><path d="M15 9v12M9 15h12" stroke="#1f78cc" stroke-width="1.2"/></svg><p>Compatible with<br>ALL PCR <b>MACHINES</b></p></li>
    <li class="feature"><svg viewBox="0 0 30 30"><circle cx="15" cy="15" r="13" fill="none" stroke="#1f78cc" stroke-width="1.6"/><path d="M10 20l5-9 5 9z" fill="none" stroke="#1f78cc" stroke-width="1.6"/></svg><p><b>Highly demanded</b><br>targets to make<br>your lab <b>more</b><br><b>appealing to providers</b></p></li>
  </ul>
  <div class="photo" role="img" aria-label="Doctor explaining a urinary tract model to a patient at a desk" style="left:245px;top:536px;width:296px;height:177px;background:linear-gradient(135deg,#9aa6ad,#e8ecef 55%,#cfd6db)"></div>
  <div class="pg-num" style="left:528px;top:752px;color:#fff">03</div>
  <div class="tab" style="left:577px;top:165px">Tabs Here - This portion will be trimmed off</div>
</section>

<!-- Page 04: Wound / sepsis -->
<section class="page page--wound">
  <svg class="shapes" viewBox="0 0 612 792">
    <defs>
      <linearGradient id="sea4" x1="0" x2="1"><stop offset="0" stop-color="#c2e8f8"/><stop offset=".6" stop-color="#4db2e8"/><stop offset="1" stop-color="#1f78cc"/></linearGradient>
      <linearGradient id="ph4" x1="0" x2="1" y1="0" y2="1"><stop offset="0" stop-color="#dde5ec"/><stop offset=".5" stop-color="#2f7fdc"/><stop offset="1" stop-color="#e6c7b2"/></linearGradient>
    </defs>
    <polygon points="290,0 612,0 612,360" fill="url(#ph4)" role="img" aria-label="Gloved clinician examining a wound on a patient's hand"/>
    <line x1="290" y1="0" x2="612" y2="362" stroke="#1f78cc" stroke-width="6"/>
    <polygon points="44,148 300,148 430,243 44,243" fill="var(--brand-blue)"/>
    <polygon points="220,792 612,690 612,792" fill="url(#sea4)"/>
    <rect x="0" y="0" width="44" height="650" fill="var(--tab-gray)"/>
    <polygon points="0,650 0,792 220,792" fill="var(--tab-gray)"/>
  </svg>
  <div class="tab" style="left:15px;top:134px">Tabs Here - This portion will be trimmed off</div>
  <div class="brand" style="left:62px;top:36px"><span class="brand__mark"></span><span class="brand__name">CEDAR PEAK LABS</span></div>
  <h1 class="page-title" style="left:66px;top:104px">Wound/Sepsis</h1>
  <div class="targets on-blue" style="left:66px;top:157px">28 TARGETS</div>
  <p class="lede on-blue" style="left:66px;top:188px;width:260px">A provider's #1 priority is their patients. When you bring them more targets, you are providing them better tools for treatment</p>
  <div class="photo" role="img" aria-label="Scientist in purple gloves inspecting a petri dish culture" style="left:60px;top:268px;width:136px;height:194px;background:linear-gradient(135deg,#c4ccd6,#8d6fd4 55%,#e9eef3)"></div>
  <div class="section" style="left:217px;top:262px">Bacteria</div>
  <ul class="list" style="left:218px;top:290px">
    <li>BACTERIA</li><li>Escherichia coli</li><li>Streptococcus agalactiae</li><li>Staphylococcus saprophyticus</li><li>Pseudomonas aeruginosa</li><li>Staphylococcus haemolyticus</li><li>Enterococcus faecium</li><li>Enterococcus faecalis</li><li>Acinetobacter calcoaceticus-<br>baumannii complex</li>
  </ul>
  <ul class="list" style="left:404px;top:290px">
    <li>Klebsiella oxytoca</li><li>Klebsiella aerogenes</li><li>Klebsiella pneumoniae</li><li>Staphylococcus aureus</li><li>Streptococcus pyogenes</li><li>Streptococcus pneumoniae</li><li>Streptococcus dysgalactiae</li><li>Staphylococcus lugdunensis</li><li>Staphylococcus epidermidis</li>
  </ul>
  <div class="section" style="left:64px;top:482px">Fungi</div>
  <ul class="list" style="left:64px;top:510px"><li>Candida krusei</li><li>Candida tropicalis</li></ul>
  <ul class="list" style="left:189px;top:510px"><li>Candida glabrata</li><li>Candida parapsilosis</li></ul>
  <ul class="list" style="left:333px;top:510px"><li>Candida albicans</li><li>Fusarium solani</li></ul>
  <ul class="list" style="left:456px;top:510px"><li>Microsporum spp</li><li>Trichophyton spp</li></ul>
  <div class="section" style="left:64px;top:563px">Antimicrobial Resistance</div>
  <ul class="list" style="left:64px;top:586px"><li>Methicillin Resistance (MecA+C)</li></ul>
  <div class="section" style="left:64px;top:612px">Viruses</div>
  <ul class="list" style="left:64px;top:637px"><li>Herpes Simplex Virus 1</li><li>Herpes Simplex Virus 2</li></ul>
  <ul class="features" style="left:328px;top:560px">
    <li class="feature"><svg viewBox="0 0 30 30"><circle cx="15" cy="15" r="13" fill="none" stroke="#1f78cc" stroke-width="1.6"/><path d="M10 20v-5M14 20v-8M18 20v-6" stroke="#1f78cc" stroke-width="2"/></svg><p><b>Cost effective</b> to help maximize<br>your lab's <b>profits</b></p></li>
    <li class="feature"><svg viewBox="0 0 30 30"><circle cx="15" cy="15" r="13" fill="none" stroke="#1f78cc" stroke-width="1.6"/><path d="M10 20v-4M14 20v-7M18 20v-10" stroke="#1f78cc" stroke-width="2"/></svg><p><b>‹45 minute</b> run time ensures<br><b>faster</b> turnaround times</p></li>
    <li class="feature"><svg viewBox="0 0 30 30"><circle cx="15" cy="15" r="13" fill="none" stroke="#1f78cc" stroke-width="1.6"/><circle cx="15" cy="15" r="6" fill="none" stroke="#1f78cc" stroke-width="1.6"/><path d="M15 9v12M9 15h12" stroke="#1f78cc" stroke-width="1.2"/></svg><p>Compatible with ALL PCR <b>MACHINES</b></p></li>
    <li class="feature"><svg viewBox="0 0 30 30"><circle cx="15" cy="15" r="13" fill="none" stroke="#1f78cc" stroke-width="1.6"/><path d="M10 20l5-9 5 9z" fill="none" stroke="#1f78cc" stroke-width="1.6"/></svg><p><b>Highly demanded</b> targets to make<br>your lab <b>more appealing to providers</b></p></li>
  </ul>
  <div class="pg-num" style="left:52px;top:729px;color:#fff">04</div>
</section>

</body>
</html>
```